Youth basketball program needs a one sided flyer to recruit new players for our competitive teams

We need a flyer to recruit players for our competitive youth basketball teams. Our program is "Lakeshore Tide Basketball" (see www.lstide-hoops.org); we are a nonprofit organization that provides opportunities to participate in youth basketball. We are focused on player development (improving each player's fundamentals and related skills.)

We are currently looking for skilled players that will be in the following grades next school year: boys 5th and 6th grade, girls 7th grade. Tryouts will occur in June - July for next season's teams. Girls season goes from October - December (break during January and February so players can play on their school teams) and March - mid April. Boys season goes from November - mid March. Interested players need to contact us to arrange a try out. During the season, teams will practice each week and play in local/regional leagues and tournaments.

We have partnered with Desmond Okafor Basketball Training (see his website at: http://www.dokskillhub.net/#!about/citr ) to provide training sessions for all our players.

We would like the following items included in the flyer: our LTB logo, reference to Desmond Okafor and the colors of green & white. The final design should emphasize our focus on player development.

Reason: Designers - thanks for the submissions thus far! I'm currently traveling abroad and haven't been able to provide adequate feedback so I'm going to extend the deadline to allow time for this. Thanks!!

Designers - thank you for all the submissions!  We were very impressed with the creativity and professionalism..  Unfortunately, we can only select one design and we have settled on the flyer/design. Thanks again for your efforts.  - Lakeshore Tide team

Target Market(s)

Boys ages 9-12, girls ages 11-13 and their respective parents.

Industry/Entity Type

Training

Requirements
Must have
• The flyer must include our Lakeshore Tide Basketball logo (can either be the colored logo or the green/white logo), our website address and the plain badge & plain badge logos to direct individuals to our web locations.

```html
<!DOCTYPE html>
<html lang="en">
<head>
<meta charset="utf-8">
<title>Lakeshore Tide Basketball – Tryouts Flyer</title>
<link rel="stylesheet" href="https://fonts.googleapis.com/css2?family=Lilita+One&family=Alegreya:wght@400;700&family=Roboto+Slab:wght@700&family=Delius&display=swap">
<style>
  :root {
    --green-deep: #1c3510;
    --green-mid: #2f4716;
    --rust: #b8610f;
    --orange: #f07a12;
    --orange-tag: #ef7d1a;
    --ink-green: #1f3c12;
    --white: #ffffff;
    --social-a: #2a56b0;
    --social-b: #5fd3f0;
  }
  * { margin: 0; padding: 0; box-sizing: border-box; }
  html, body { width: 849px; height: 1200px; overflow: hidden; background: var(--white); }
  .flyer { position: relative; width: 849px; height: 1200px; overflow: hidden; background: var(--white); }

  .side-panel {
    position: absolute; left: 0; top: 0; width: 426px; height: 1200px; overflow: hidden;
    background: linear-gradient(180deg, var(--green-deep) 0%, var(--green-mid) 55%, #6a5a14 80%, var(--rust) 100%);
    color: var(--white);
    font-family: "Alegreya", Georgia, serif;
  }
  .ball-art { position: absolute; left: 0; top: 0; width: 426px; height: 560px; }

  .tryout-tag {
    position: absolute; left: 48px; top: 528px; width: 222px; height: 126px;
    background: var(--orange-tag); border-radius: 8px;
    transform: rotate(-8deg);
    box-shadow: 2px 3px 6px rgba(0,0,0,.35);
    display: flex; align-items: center; justify-content: center; text-align: center;
    font-family: "Delius", "Comic Sans MS", cursive;
    font-size: 27px; line-height: 27px; color: var(--white);
  }

  .contact { position: absolute; left: 18px; top: 748px; }
  .contact .lead { font-size: 27px; line-height: 29px; margin-bottom: 16px; }
  .contact .details { font-size: 23px; line-height: 25px; }

  .partners { position: absolute; left: 24px; top: 1012px; font-size: 16px; line-height: 15px; }

  .social { position: absolute; left: 25px; font-size: 13px; display: flex; align-items: center; gap: 10px; }
  .social .badge { width: 72px; height: 22px; display: inline-block; }
  .social.fb { top: 1068px; } .social.fb .badge { background: var(--social-a); border: 2px solid var(--white); }
  .social.tw { top: 1097px; } .social.tw .badge { background: var(--social-b); }

  .info { position: absolute; left: 426px; top: 0; width: 423px; height: 1200px; text-align: center; color: var(--ink-green); font-family: "Alegreya", Georgia, serif; }
  .title { position: absolute; top: 82px; left: 0; width: 376px; font-family: "Lilita One", Impact, sans-serif; text-shadow: 1px 2px 2px rgba(0,0,0,.3); }
  .title .top { display: block; font-size: 30px; line-height: 34px; }
  .title .main { display: block; font-size: 74px; line-height: 72px; color: var(--orange); -webkit-text-stroke: 2px var(--ink-green); letter-spacing: 1px; }
  .title .bottom { display: block; font-size: 46px; line-height: 46px; }

  .intro { position: absolute; top: 256px; left: 22px; width: 344px; font-size: 27px; line-height: 25px; text-shadow: 1px 2px 2px rgba(0,0,0,.25); }
  .grades { position: absolute; top: 374px; left: 40px; width: 340px; font-family: "Roboto Slab", Georgia, serif; font-size: 27px; line-height: 26px; }
  .seasons { position: absolute; top: 458px; left: 40px; width: 332px; font-size: 28px; line-height: 26.5px; }
  .practice { position: absolute; top: 720px; left: 46px; width: 322px; font-size: 22px; line-height: 26px; }

  .club-mark { position: absolute; left: 104px; top: 930px; width: 236px; display: flex; flex-direction: column; align-items: center; gap: 12px; }
  .club-mark .dot { width: 150px; height: 150px; border-radius: 50%; background: var(--orange); }
  .club-mark .name { font-family: "Alegreya", Georgia, serif; font-weight: 700; font-size: 24px; color: var(--ink-green); }
</style>
</head>
<body>
<main class="flyer">
  <section class="side-panel">
    <svg class="ball-art" viewBox="0 0 426 560" role="img" aria-label="Close-up photograph of an orange basketball">
      <defs>
        <radialGradient id="ballTone" cx="0.62" cy="0.32" r="0.75">
          <stop offset="0" stop-color="#f6b24a"/>
          <stop offset="0.45" stop-color="#e56a12"/>
          <stop offset="1" stop-color="#a8360a"/>
        </radialGradient>
      </defs>
      <circle cx="215" cy="232" r="300" fill="url(#ballTone)"/>
    </svg>

    <div class="tryout-tag">Tryouts will<br>occur in<br>June/July for<br>next season's<br>teams.</div>

    <div class="contact">
      <p class="lead">Interested players need&nbsp; to<br>contact us to arrange a try out.</p>
      <p class="details">Contact Marcus at 555.218.7302<br>or at hello@lstide-hoops.org<br>website: http://www.lstide-hoops.org/</p>
    </div>

    <p class="partners">Partners: Desmond Okafor Basketball Training<br>http://www.dokskillhub.net/#!about/citr</p>

    <p class="social fb"><span class="badge"></span>Lakeshore-Tide-Basketball-Inc</p>
    <p class="social tw"><span class="badge"></span>@LSTideHoops</p>
  </section>

  <section class="info">
    <h1 class="title">
      <span class="top">Lakeshore</span>
      <span class="main">TIDE</span>
      <span class="bottom">Basketball</span>
    </h1>
    <p class="intro">We are currently looking for skilled players that will be in the following grades next school year:</p>
    <p class="grades">Boys 5th and 6th grade,<br>Girls 7th grade.</p>
    <p class="seasons">Girls season goes from October to December (break during January and February so players can play on their school teams) and from March to mid April. Boys season goes from November to mid March.</p>
    <p class="practice">During the season, teams will practice each week and play in local/regional leagues and tournaments.</p>
    <div class="club-mark">
      <span class="dot"></span>
      <span class="name">Lakeshore Tide</span>
    </div>
  </section>
</main>
</body>
</html>
```